Booklet Design needed for Copperleaf Digital Studio

A Little bit about us:
At Copperleaf Digital Studio we offer our clients the very best in their website needs without the big price tag.

We take the hassle out of setting up a website and take care of the website design, domain registration, SEO and hosting.
We know how important it is to have a Visually Appealing website, that’s why when we are designing our websites we focus on the main things like branding, content, creativity, colors, layout, ease of use, and imagery.

Design Specifics:
I currently have two booklets that I give to my clients:
one before I start designing their site as a general information booklet
and the other one I give only once I complete their site - which is about how to use my editor.

I want to jazz these two booklets up and bit with a modern and professional look, and I want both the booklets to have a similar design, I would also like it to be a similar look to my website, www.copperleafdigitalstudio.com.au.

Previously the budget was AUD$130. Now it is AUD$260.
This reflects your creative effort for 2 booklets.

I have uploaded the two booklets, labeled Booklet 1 (7 pages) and Booklet 2 (15 pages), inside you will find the information and images I want on each page.
The booklets also need a title page.

Thanks Designers. Will appreciate all your creative effort!

Hi Designers . i have updated the content for one of the booklets. the new file which i will upload shortly is called "New Client information Booklet content update". please use this for one of the booklets to be designed. the other booklet still needs to be done (the one with the editor information inside)Cheers Added Thursday, October 29, 2015

Target Market(s)

Small to medium Businesses

Font styles to use
Sans Serif

Colors
3176b5
5c5c5c
ffffff

Requirements
Must have
• Logo, images and content from original booklets. And the Seperate booklets for the two different booklets. Similar modern, professional design.
Nice to have
• Moder, professional design, similar look to my website. Www.copperleafdigitalstudio.com.au

```html
<!DOCTYPE html>
<html lang="en">
<head>
<meta charset="utf-8">
<title>Copperleaf Digital Studio – Booklet Cover Spread</title>
<link href="https://fonts.googleapis.com/css2?family=Open+Sans:wght@400;600;700;800&family=Indie+Flower&display=swap" rel="stylesheet">
<style>
  :root {
    --bg: #e6e8eb;
    --band-blue: #29a3e0;
    --deep-blue: #1f5d99;
    --mid-blue: #3176b5;
    --soft-blue: #79b3e2;
    --panel-dark: #222426;
    --ink-grey: #5c5c5c;
    --white: #ffffff;
  }
  * { box-sizing: border-box; margin: 0; padding: 0; }
  html, body { width: 1200px; height: 942px; overflow: hidden; }
  body {
    background: var(--bg);
    font-family: "Open Sans", Arial, sans-serif;
    color: var(--white);
  }
  .spread {
    position: absolute;
    left: 40px;
    top: 75px;
    width: 1120px;
    height: 792px;
    display: flex;
    box-shadow: 0 6px 24px rgba(0,0,0,.18);
  }
  .page {
    position: relative;
    width: 560px;
    height: 792px;
    overflow: hidden;
  }
  .page-art { position: absolute; inset: 0; width: 100%; height: 100%; }

  /* Back cover */
  .aim-panel {
    position: absolute;
    left: 0; top: 34px;
    width: 520px; height: 172px;
    padding: 12px 20px 0;
    text-align: center;
    font-size: 9.5px;
    line-height: 1.35;
    overflow: hidden;
  }
  .aim-title { font-size: 13px; font-weight: 700; letter-spacing: .5px; line-height: 1.4; }
  .aim-subtitle { font-size: 12.5px; font-weight: 700; margin-top: 4px; line-height: 1.35; }
  .aim-intro { margin-top: 1px; }

  .back-footer {
    position: absolute;
    left: 0; bottom: 0;
    width: 560px; height: 140px;
  }
  .wordmark {
    font-weight: 800;
    color: var(--white);
    letter-spacing: .5px;
    line-height: 1.05;
    text-transform: uppercase;
  }
  .back-footer .wordmark {
    position: absolute;
    left: 28px; top: 44px;
    width: 230px;
    font-size: 19px;
  }
  .contact-divider {
    position: absolute;
    left: 268px; top: 30px;
    width: 5px; height: 78px;
    background: var(--panel-dark);
  }
  .contact {
    position: absolute;
    left: 286px; top: 24px;
    font-size: 12px;
    line-height: 1.3;
  }
  .contact dt { font-weight: 700; }
  .contact dd { font-weight: 400; }

  /* Front cover */
  .front-tab {
    position: absolute;
    right: 0; top: 30px;
    width: 250px; height: 52px;
    display: flex; align-items: center; justify-content: center;
  }
  .front-tab .wordmark { font-size: 15px; }
  .tagline {
    position: absolute;
    left: 150px; top: 190px;
    width: 380px;
    font-family: "Indie Flower", cursive;
    font-size: 40px;
    font-weight: 400;
    line-height: 1.35;
    text-align: center;
    color: var(--white);
  }
  .site-url {
    position: absolute;
    right: 22px; bottom: 64px;
    font-size: 19px;
    font-weight: 700;
    color: var(--white);
  }
</style>
</head>
<body>
<main class="spread">

  <section class="page back-cover">
    <svg class="page-art" viewBox="0 0 560 792" role="img" aria-label="Soft blue bokeh light backdrop between light blue bands">
      <defs>
        <radialGradient id="bokeh-back" cx="55%" cy="45%" r="75%">
          <stop offset="0" stop-color="var(--soft-blue)"/>
          <stop offset="1" stop-color="var(--deep-blue)"/>
        </radialGradient>
      </defs>
      <rect width="560" height="792" fill="var(--band-blue)"/>
      <path d="M0 190 H560 V612 C500 612 490 652 440 652 H0 Z" fill="url(#bokeh-back)"/>
      <path d="M0 652 H440 C490 652 500 612 560 612" fill="none" stroke="var(--white)" stroke-width="5"/>
      <path d="M0 34 H520 V186 Q520 206 500 206 H0 Z" fill="var(--panel-dark)"/>
    </svg>

    <div class="aim-panel">
      <p class="aim-title">OUR AIM</p>
      <p class="aim-intro">We take the hassle out of setting up a website and take care of the website design, domain registration, SEO and hosting.</p>
      <p class="aim-subtitle">We aim:</p>
      <p>To design a website that the client will love</p>
      <p>To listen to our Clients and ensure that they get the website they want and have it looking exactly how they wish.</p>
      <p>To produce smart looking, Visually Appealing, high quality website at an affordable price, for your Clients Businesses.</p>
      <p>To produce website with out the big price tag</p>
    </div>

    <footer class="back-footer">
      <p class="wordmark">Copperleaf Digital Studio</p>
      <span class="contact-divider"></span>
      <dl class="contact">
        <dt>Phone:</dt>
        <dd>0412 555 018</dd>
        <dt>General Enquiries:</dt>
        <dd>enquiries@copperleafdigitalstudio.com.au</dd>
        <dt>Support:</dt>
        <dd>support@copperleafdigitalstudio.com.au</dd>
      </dl>
    </footer>
  </section>

  <section class="page front-cover">
    <svg class="page-art" viewBox="0 0 560 792" role="img" aria-label="Soft blue bokeh light backdrop between light blue bands">
      <defs>
        <radialGradient id="bokeh-front" cx="50%" cy="45%" r="75%">
          <stop offset="0" stop-color="var(--soft-blue)"/>
          <stop offset="1" stop-color="var(--deep-blue)"/>
        </radialGradient>
      </defs>
      <rect width="560" height="792" fill="var(--band-blue)"/>
      <path d="M0 60 C60 60 70 48 120 48 H560 V580 H120 C70 580 60 612 0 612 Z" fill="url(#bokeh-front)"/>
      <path d="M0 60 C60 60 70 48 120 48 H560" fill="none" stroke="var(--white)" stroke-width="4"/>
      <path d="M0 612 C60 612 70 580 120 580 H560" fill="none" stroke="var(--white)" stroke-width="5"/>
      <path d="M310 30 H560 V82 H330 Q310 82 310 62 Z" fill="var(--panel-dark)"/>
    </svg>

    <div class="front-tab">
      <p class="wordmark">Copperleaf Digital Studio</p>
    </div>

    <h1 class="tagline">"We Design Websites that get results"</h1>

    <p class="site-url">www.copperleafdigitalstudio.com.au.</p>
  </section>

</main>
</body>
</html>
```